International horse riding portal needs web design

We are looking for the web design for the new "Feldmoor" web portal.

Offers from the world of horses and riding should be found on this portal, eg from the categories riding schools, riding holidays, farriers, riding stables, riding stables. And all information about riding.

It is important that the different areas can be found easily and clearly. For some categories, some features should already be available in the search bar.

In addition, the design should make you want to go horse riding. The user should be emotionally picked up on the landing page.

In the lower area, some offers should be advertised, eg from the areas of riding holidays, riding training, and horse trading.

Please use the colors from the logo for the design.
C100 M50 Y10 K50 and C0 M20 Y60 K30

```html
<!DOCTYPE html>
<html lang="en">
<head>
<meta charset="utf-8">
<title>Feldmoor – Horse Riding Portal</title>
<link href="https://fonts.googleapis.com/css2?family=Cinzel:wght@400;700&family=Arimo:wght@400;700&display=swap" rel="stylesheet">
<style>
:root{
  --navy:#0d3a66;
  --navy-dark:#0b3360;
  --gold:#b3915a;
  --gold-dark:#8a6d3f;
  --ink:#333;
  --muted:#666;
  --beige:#f6f1e6;
  --white:#fff;
}
*{margin:0;padding:0;box-sizing:border-box}
html,body{width:1200px;height:3820px;overflow:hidden}
body{position:relative;font-family:"Arimo",Arial,sans-serif;color:var(--ink);background:var(--white)}
.serif{font-family:"Cinzel",Georgia,serif}
.abs{position:absolute}

/* hero */
.hero{left:0;top:0;width:1200px;height:801px;
  background:radial-gradient(ellipse at 65% 40%,#7a4526 0%,#4a2a18 30%,#2a1a12 60%,#1a120d 100%)}
.hero-person{left:620px;top:420px;width:580px;height:381px;
  background:radial-gradient(ellipse at 60% 60%,rgba(150,60,80,.55),rgba(80,30,40,0) 70%)}

/* header */
.header{left:111px;top:0;width:978px;height:165px;background:var(--white)}
.brand{left:0;top:0;width:230px;height:165px;display:flex;align-items:center;justify-content:center;gap:10px}
.brand-dot{width:16px;height:16px;border-radius:50%;background:var(--gold)}
.brand-name{font-family:"Cinzel",Georgia,serif;font-weight:700;font-size:30px;color:var(--navy);letter-spacing:1px}
.topnav{left:276px;top:40px;display:flex;gap:31px;font-family:"Cinzel",Georgia,serif;font-size:13px;font-weight:700;color:#333}
.search{left:556px;top:24px;width:309px;height:49px;border:1px solid #bbb;border-radius:25px;overflow:hidden;display:flex}
.search span{flex:1;padding:16px 18px;font-size:14px;color:#555}
.search b{width:72px;background:var(--navy);color:#fff;display:flex;align-items:center;justify-content:center;font-size:16px}
.login{left:871px;top:25px;width:98px;height:46px;border-radius:23px;background:var(--gold);color:#fff;font-family:"Cinzel",Georgia,serif;font-weight:700;font-size:14px;display:flex;align-items:center;justify-content:center}
.rule{left:240px;top:95px;width:738px;height:1px;background:#ddd}
.subnav{left:250px;top:123px;width:716px;display:flex;justify-content:space-between;font-family:"Cinzel",Georgia,serif;font-size:12.5px;font-weight:700;color:#333}

/* search panel */
.finder{left:89px;top:317px;width:580px;height:355px;border:3px solid var(--gold-dark);background:rgba(30,20,15,.35)}
.tabs{left:16px;top:12px;display:flex;gap:7px}
.tab{width:104px;height:61px;background:#3c3c3c;color:#fff;font-family:"Cinzel",Georgia,serif;font-weight:700;font-size:13px;line-height:17px;display:flex;align-items:center;justify-content:center;text-align:center}
.tab.active{background:#2a2420;border:1px solid var(--gold);position:relative}
.tab.active::after{content:"";position:absolute;left:46px;bottom:-8px;border:7px solid transparent;border-top-color:var(--gold);border-bottom:0}
.field{width:266px;height:40px;border:1px solid #555;background:rgba(20,16,14,.6);color:#fff;font-family:"Cinzel",Georgia,serif;font-weight:700;font-size:13px;padding:12px 16px}
.find-btn{left:16px;top:281px;width:156px;height:44px;background:var(--gold-dark);color:#fff;font-family:"Cinzel",Georgia,serif;font-weight:700;font-size:16px;display:flex;align-items:center;justify-content:center}

/* intro */
.intro{left:0;top:856px;width:1200px;text-align:center}
.intro h2{font-family:"Cinzel",Georgia,serif;color:var(--navy);font-size:22px;letter-spacing:1px}
.intro h3{font-family:"Cinzel",Georgia,serif;color:var(--gold);font-size:30px;font-weight:400;letter-spacing:1px;margin-top:10px}
.intro p{width:780px;margin:30px auto 0;font-size:15px;line-height:30px;color:#555}

/* features */
.row{left:111px;width:978px;height:329px}
.photo{position:absolute;top:0;width:489px;height:329px}
.copy{position:absolute;top:0;width:489px;height:329px;padding:28px 34px 0 45px}
.copy h4{font-family:"Cinzel",Georgia,serif;font-size:28px;color:var(--navy);letter-spacing:1px}
.copy .bar{width:60px;height:3px;background:var(--navy);margin:14px 0 28px}
.copy p{font-size:13.5px;line-height:26px;color:#555;text-align:justify}
.outline{display:inline-flex;margin-top:26px;height:43px;padding:0 14px;border:1.5px solid var(--navy);border-radius:4px;align-items:center;font-family:"Cinzel",Georgia,serif;font-weight:700;font-size:14px;color:var(--navy)}

/* offers */
.offers{left:0;top:2789px;width:1200px;height:648px;background:var(--beige)}
.offers h2{position:absolute;top:80px;width:100%;text-align:center;font-family:"Cinzel",Georgia,serif;font-size:31px;color:var(--navy);letter-spacing:1px}
.card{top:148px;width:304px;height:445px;background:#fff;border:1px solid #ece6da}
.card .corner{position:absolute;left:-3px;top:-3px;width:100px;height:80px;border-left:5px solid var(--gold);border-top:5px solid var(--gold)}
.card .pic{position:absolute;left:20px;top:24px;width:264px;height:206px}
.card .tag{position:absolute;left:33px;top:36px;background:rgba(179,145,90,.9);color:#fff;font-family:"Cinzel",Georgia,serif;font-size:13px;padding:4px 8px}
.card p{position:absolute;left:20px;top:258px;width:264px;text-align:center;font-size:15px;line-height:28px;color:#555}
.solid{position:absolute;left:90px;top:360px;width:124px;height:44px;background:var(--navy);color:#fff;font-family:"Cinzel",Georgia,serif;font-weight:700;font-size:15px;display:flex;align-items:center;justify-content:center}

/* footer */
.footer{left:0;top:3437px;width:1200px;height:383px;background:var(--navy-dark);color:#fff}
.contact{top:44px;width:260px;text-align:center}
.contact .ring{width:67px;height:67px;border:2px solid #fff;border-radius:50%;margin:0 auto;display:flex;align-items:center;justify-content:center}
.contact h5{font-family:"Cinzel",Georgia,serif;font-weight:400;font-size:20px;margin-top:16px;letter-spacing:1px}
.contact p{font-size:13px;line-height:21px;margin-top:4px}
.frule{left:111px;top:234px;width:978px;height:1px;background:rgba(255,255,255,.25)}
.fbrand{left:160px;top:262px;width:190px;height:100px;display:flex;align-items:center;justify-content:center;gap:10px}
.fbrand .brand-name{color:#fff;font-size:28px}
.flinks{left:446px;top:276px;width:643px;display:flex;justify-content:space-between;font-family:"Cinzel",Georgia,serif;font-weight:700;font-size:12.5px}
.copyright{left:446px;top:323px;width:643px;text-align:center;font-family:"Cinzel",Georgia,serif;font-size:14px}
</style>
</head>
<body>

<div class="abs hero" role="img" aria-label="Photo of a woman gently kissing a chestnut horse in a dark stable"></div>

<header class="abs header">
  <div class="abs brand"><span class="brand-dot"></span><span class="brand-name">Feldmoor</span></div>
  <nav class="abs topnav"><span>HOME</span><span>ABOUT US</span><span>CONTACT US</span></nav>
  <div class="abs search"><span>Search</span><b>FIND</b></div>
  <div class="abs login">LOGIN</div>
  <div class="abs rule"></div>
  <nav class="abs subnav"><span>RIDING SCHOOLS</span><span>RIDING HOLIDAYS</span><span>FARRIERS</span><span>RIDING STABLES</span><span>RIDING STABLES</span><span>MORE</span></nav>
</header>

<section class="abs finder">
  <div class="abs tabs">
    <div class="tab active">RIDING<br>SCHOOLS</div>
    <div class="tab">RIDING<br>HOLIDAYS</div>
    <div class="tab">FARRIERS</div>
    <div class="tab">RIDING<br>STABLES</div>
    <div class="tab">RIDING<br>STABLES</div>
  </div>
  <div class="abs field" style="left:16px;top:113px">FEATURE 1</div>
  <div class="abs field" style="left:294px;top:113px">FEATURE 2</div>
  <div class="abs field" style="left:16px;top:165px">FEATURE 3</div>
  <div class="abs field" style="left:294px;top:165px">FEATURE 4</div>
  <div class="abs field" style="left:16px;top:217px">ZIP</div>
  <div class="abs field" style="left:294px;top:217px">CITY</div>
  <div class="abs find-btn">FIND</div>
</section>

<section class="abs intro">
  <h2>IHIC TECTIO BLAB INCIENIS AUT HILIQUO</h2>
  <h3>QUISQUI AEPRECTUR? URESEQUOD QUI DITIS</h3>
  <p>Udi officipsamus dolut alicimillam fugit faceseq uodisquati suntemod eum id ut ullatquam aceat. Ibus. Dus. Erferup tatemo exererum, eum voloren Udi officipsamus dolut alicimillam fugit faceseq uodisquati suntemod eum id ut ullatquam aceat. Ibus. Dus. Erferup tatemo exererum, eum voloren</p>
</section>

<section class="abs row" style="top:1117px">
  <div class="photo" style="left:0;background:linear-gradient(180deg,#7d9a5a 0%,#a9a07a 50%,#d8cdb5 100%)" role="img" aria-label="Photo of a girl riding a chestnut pony on a lunge line in a sandy arena"></div>
  <div class="copy" style="left:489px">
    <h4>RIDING SCHOOLS</h4><div class="bar"></div>
    <p>Sed ut perspiciatis unde omnis iste natus error sit voluptatem accu santium doloremque laudantium, totam rem aperiam, eaque ipsa quae ab illo inventore veritatis et quasi architecto beatae vitae dicta sunt explicabo. Nemo enim ipsam voluptatem quia voluptas sit aspernatur aut odit aut fugit, sed quia consequuntur.....</p>
    <span class="outline">READ MORE</span>
  </div>
</section>

<section class="abs row" style="top:1445px">
  <div class="copy" style="left:0">
    <h4>RIDING HOLIDAYS</h4><div class="bar"></div>
    <p>Sed ut perspiciatis unde omnis iste natus error sit voluptatem accu santium doloremque laudantium, totam rem aperiam, eaque ipsa quae ab illo inventore veritatis et quasi architecto beatae vitae dicta sunt explicabo. Nemo enim ipsam voluptatem quia voluptas sit aspernatur aut odit aut fugit, sed quia consequuntur.....</p>
    <span class="outline">READ MORE</span>
  </div>
  <div class="photo" style="left:489px;background:linear-gradient(180deg,#6e6a7a 0%,#c79a86 45%,#3a3038 100%)" role="img" aria-label="Photo of a woman on a dark horse at the beach at sunset"></div>
</section>

<section class="abs row" style="top:1774px">
  <div class="photo" style="left:0;background:linear-gradient(135deg,#2a2a2a 0%,#7a7570 50%,#3a3530 100%)" role="img" aria-label="Photo of a farrier fitting a hot horseshoe with tongs amid smoke"></div>
  <div class="copy" style="left:489px">
    <h4>FARRIERS</h4><div class="bar"></div>
    <p>Sed ut perspiciatis unde omnis iste natus error sit voluptatem accu santium doloremque laudantium, totam rem aperiam, eaque ipsa quae ab illo inventore veritatis et quasi architecto beatae vitae dicta sunt explicabo. Nemo enim ipsam voluptatem quia voluptas sit aspernatur aut odit aut fugit, sed quia consequuntur.....</p>
    <span class="outline">READ MORE</span>
  </div>
</section>

<section class="abs row" style="top:2102px">
  <div class="copy" style="left:0">
    <h4>RIDING STABLES</h4><div class="bar"></div>
    <p>Sed ut perspiciatis unde omnis iste natus error sit voluptatem accu santium doloremque laudantium, totam rem aperiam, eaque ipsa quae ab illo inventore veritatis et quasi architecto beatae vitae dicta sunt explicabo. Nemo enim ipsam voluptatem quia voluptas sit aspernatur aut odit aut fugit, sed quia consequuntur.....</p>
    <span class="outline">READ MORE</span>
  </div>
  <div class="photo" style="left:489px;background:linear-gradient(90deg,#3a2a22 0%,#7a4a30 40%,#c9b49a 100%)" role="img" aria-label="Photo of a bay horse looking out of a stable stall"></div>
</section>

<section class="abs row" style="top:2430px">
  <div class="photo" style="left:0;background:linear-gradient(135deg,#4a2e1a 0%,#b0703a 45%,#2e2a30 100%)" role="img" aria-label="Photo of a rider in a yellow jacket grooming a chestnut horse in a barn"></div>
  <div class="copy" style="left:489px">
    <h4>RIDING STABLES</h4><div class="bar"></div>
    <p>Sed ut perspiciatis unde omnis iste natus error sit voluptatem accu santium doloremque laudantium, totam rem aperiam, eaque ipsa quae ab illo inventore veritatis et quasi architecto beatae vitae dicta sunt explicabo. Nemo enim ipsam voluptatem quia voluptas sit aspernatur aut odit aut fugit, sed quia consequuntur.....</p>
    <span class="outline">READ MORE</span>
  </div>
</section>

<section class="abs offers">
  <h2>IHIC TECTIO BLAB INCIENIS AUT</h2>
  <article class="abs card" style="left:111px">
    <div class="corner"></div>
    <div class="pic" style="background:linear-gradient(135deg,#3a2418 0%,#8a4e2c 55%,#c08a5a 100%)" role="img" aria-label="Photo of a bay horse with a bridle in autumn light"></div>
    <span class="tag">LAND | REGION</span>
    <p>Udi officipsamus dolut alicimillam fugit faceseq uodisquati suntemod eum id ut ullatquam aceat</p>
    <span class="solid">Read More</span>
  </article>
  <article class="abs card" style="left:448px">
    <div class="corner"></div>
    <div class="pic" style="background:linear-gradient(180deg,#3e5a32 0%,#7a7a5a 55%,#b8a890 100%)" role="img" aria-label="Photo of a young rider jumping a pony over a pole with a trainer"></div>
    <span class="tag">LAND | REGION</span>
    <p>Udi officipsamus dolut alicimillam fugit faceseq uodisquati suntemod eum id ut ullatquam aceat</p>
    <span class="solid">Read More</span>
  </article>
  <article class="abs card" style="left:785px">
    <div class="corner"></div>
    <div class="pic" style="background:linear-gradient(180deg,#4a5a72 0%,#6e7a3e 50%,#7a5a8a 100%)" role="img" aria-label="Photo of a brown horse in a meadow of purple flowers"></div>
    <span class="tag">LAND | REGION</span>
    <p>Udi officipsamus dolut alicimillam fugit faceseq uodisquati suntemod eum id ut ullatquam aceat</p>
    <span class="solid">Read More</span>
  </article>
</section>

<footer class="abs footer">
  <div class="abs contact" style="left:151px">
    <div class="ring"><svg width="16" height="22" viewBox="0 0 16 22"><path d="M8 1a7 7 0 0 0-7 7c0 5 7 13 7 13s7-8 7-13a7 7 0 0 0-7-7z" fill="none" stroke="#fff" stroke-width="2"/><circle cx="8" cy="8" r="2.5" fill="#fff"/></svg></div>
    <h5>LOCATION</h5>
    <p>265 Lorem Ipsum Dummy Lorem<br>Ipsum Dummy</p>
  </div>
  <div class="abs contact" style="left:482px">
    <div class="ring"><svg width="18" height="18" viewBox="0 0 24 24"><path d="M6.6 10.8a15 15 0 0 0 6.6 6.6l2.2-2.2c.3-.3.7-.4 1-.2 1.1.4 2.3.6 3.6.6.6 0 1 .4 1 1V20c0 .6-.4 1-1 1A17 17 0 0 1 3 4c0-.6.4-1 1-1h3.5c.6 0 1 .4 1 1 0 1.3.2 2.5.6 3.6.1.3 0 .7-.2 1z" fill="#fff"/></svg></div>
    <h5>CONTACT</h5>
    <p>+1 000 000 0000</p>
  </div>
  <div class="abs contact" style="left:815px">
    <div class="ring"><svg width="18" height="14" viewBox="0 0 18 14"><rect x="0" y="0" width="18" height="14" rx="1.5" fill="#fff"/><path d="M1 1l8 6 8-6" fill="none" stroke="#0b3360" stroke-width="1.6"/></svg></div>
    <h5>EMAIL</h5>
    <p>info@feldmoor-riding.net</p>
  </div>
  <div class="abs frule"></div>
  <div class="abs fbrand"><span class="brand-dot"></span><span class="brand-name">Feldmoor</span></div>
  <nav class="abs flinks"><span>RIDING SCHOOLS</span><span>RIDING HOLIDAYS</span><span>FARRIERS</span><span>RIDING STABLES</span><span>RIDING STABLES</span></nav>
  <div class="abs copyright">© Copyright 2022 Feldmoor.All rights reserved.</div>
</footer>

</body>
</html>
```